Real estate company needs a card that makes you say WOW!

We need an awesome business card for our real estate company, Stonebrook Realty Partners of Chicago, that will stand out from the crowd. We specialize in buying and selling real estate, property management, and real estate investments (Flips & Rentals). On the business card, I need the following:

- Our logo
- Services
- My name & contact info (Derek Ollanby, 630-517-2946, Derek@StonebrookRPC.com)
- My title (Director of Acquisitions)
- StonebrookRPC.com

I attached an EPS file of our logo. Let me know if you have any questions. Thank you in advance!

```html
<!DOCTYPE html>
<html lang="en">
<head>
<meta charset="utf-8">
<title>Stonebrook Realty Partners of Chicago – Business Card</title>
<link rel="stylesheet" href="https://fonts.googleapis.com/css2?family=Tinos:wght@400;700&family=Bitter:wght@400;500&display=swap">
<style>
  :root {
    --brand-blue: #1465ad;
    --brand-blue-deep: #0b4f8f;
    --brand-blue-light: #2a86cc;
    --swoosh-grey: #8d8f93;
    --swoosh-grey-light: #c9cacc;
    --card-white: #ffffff;
    --backdrop: #e9e9eb;
  }
  * { box-sizing: border-box; margin: 0; padding: 0; }
  html, body {
    width: 1200px; height: 471px; overflow: hidden;
    background: var(--backdrop);
  }
  .canvas {
    position: relative; width: 1200px; height: 471px;
  }
  .card {
    position: absolute; top: 70px;
    width: 540px; height: 330px;
    border-radius: 24px; overflow: hidden;
    box-shadow: 0 6px 18px rgba(0,0,0,0.18);
  }
  .card--front { left: 40px; background: var(--card-white); }
  .card--back {
    left: 620px;
    background: radial-gradient(ellipse at 50% 40%, var(--brand-blue-light) 0%, var(--brand-blue) 55%, var(--brand-blue-deep) 100%);
    color: var(--card-white);
    text-align: center;
  }
  .card__waves { position: absolute; inset: 0; width: 100%; height: 100%; }

  .brand-name {
    font-family: "Tinos", serif; font-weight: 400;
    letter-spacing: 1px; line-height: 1.1;
  }
  .card--front .brand-name {
    position: absolute; left: 36px; top: 70px;
    font-size: 27px; color: var(--brand-blue);
  }
  .card--back .brand-name {
    margin-top: 78px; font-size: 30px; color: var(--card-white);
  }

  .contact {
    position: absolute; right: 24px; top: 150px;
    text-align: right; color: var(--card-white);
    font-family: "Tinos", serif;
  }
  .contact__name { font-weight: 700; font-size: 22px; }
  .contact__title { font-size: 11px; margin-top: 2px; }
  .contact__list { list-style: none; margin-top: 22px; font-size: 14.5px; }
  .contact__list li {
    display: flex; justify-content: flex-end; align-items: center;
    gap: 5px; margin-bottom: 8px;
  }
  .contact__icon { width: 13px; height: 13px; }

  .services {
    font-family: "Bitter", serif; font-size: 14px; line-height: 1.45;
    margin-top: 24px;
  }
  .services__lead { display: block; }
  .website {
    font-family: "Bitter", serif; font-weight: 500; font-size: 19px;
    margin-top: 22px; letter-spacing: 0.3px;
  }
</style>
</head>
<body>
<main class="canvas">

  <section class="card card--front" aria-label="Business card front">
    <svg class="card__waves" viewBox="0 0 540 330" preserveAspectRatio="none" aria-hidden="true">
      <path d="M0,255 C150,300 230,210 320,150 C390,105 460,95 540,100" fill="none" stroke="var(--swoosh-grey-light)" stroke-width="14"/>
      <path d="M0,330 L0,285 C130,300 220,240 300,180 C370,130 450,112 540,115 L540,330 Z" fill="var(--brand-blue)"/>
      <path d="M0,285 C130,300 220,240 300,180 C370,130 450,112 540,115" fill="none" stroke="var(--swoosh-grey)" stroke-width="4"/>
      <path d="M0,300 C120,322 230,300 300,250" fill="none" stroke="var(--swoosh-grey-light)" stroke-width="10"/>
      <path d="M0,318 C140,330 250,300 320,240" fill="none" stroke="var(--card-white)" stroke-width="3"/>
    </svg>

    <h1 class="brand-name">Stonebrook Realty Partners<br>of Chicago</h1>

    <div class="contact">
      <p class="contact__name">Derek Ollanby</p>
      <p class="contact__title">Director of Acquisitions</p>
      <ul class="contact__list">
        <li>
          <svg class="contact__icon" viewBox="0 0 16 16" aria-hidden="true"><circle cx="8" cy="8" r="7.5" fill="#fff"/><path d="M5 4 l2 0 1 2.5 -1.2 1 a6 6 0 0 0 2.5 2.5 l1-1.2 2.5 1 0 2 c-4 .5 -8.5 -4 -7.8 -7.8z" fill="var(--brand-blue)"/></svg>
          630-517-2946
        </li>
        <li>
          <svg class="contact__icon" viewBox="0 0 16 16" aria-hidden="true"><circle cx="8" cy="8" r="7.5" fill="#fff"/><rect x="3.5" y="5" width="9" height="6.5" fill="var(--brand-blue)"/><path d="M3.5 5 L8 9 L12.5 5" fill="none" stroke="#fff" stroke-width="1"/></svg>
          Derek@StonebrookRPC.com
        </li>
        <li>
          <svg class="contact__icon" viewBox="0 0 16 16" aria-hidden="true"><circle cx="8" cy="8" r="7" fill="none" stroke="#fff" stroke-width="1.5"/><ellipse cx="8" cy="8" rx="3" ry="7" fill="none" stroke="#fff" stroke-width="1.2"/><path d="M1 8 H15" stroke="#fff" stroke-width="1.2"/></svg>
          www.StonebrookRPC.com
        </li>
      </ul>
    </div>
  </section>

  <section class="card card--back" aria-label="Business card back">
    <h2 class="brand-name">Stonebrook Realty Partners<br>of Chicago</h2>
    <p class="services">
      <span class="services__lead">We Specialize In</span>
      Buying &amp; Selling Real Estate, Property Management,<br>
      And Real Estate Investments (Flips &amp; Rentals).
    </p>
    <p class="website">www.StonebrookRPC.com</p>
  </section>

</main>
</body>
</html>
```